Events and Parties web-site needs a Web Design

VoTrel needs a web design.
VoTrel means The Bees in Italian.
VoTrel target market is people who is organizing parties and events.
Our mission is that the parties and events of our clients exceed their expectations by providing them web and mobile tools.
Our vision is to be the best and biggest party web portal of the country.
The main features of our web site is to let people invite guests and search suppliers/providers. Guests will also confirm presence (RSVP) and buy presents/gifts at the site as well.
Our slogan is "Curta sua festa desde já !" that means "Enjoy our party now !" in Brazilian Portuguese.
The idea here is that the party starts now and not only at the scheduled date and time.
Updates
It seems that must have and nice to have briefing is not appearing to you as I filled. So I will type it agai here:
Our slogan text that is "Curta sua festa desde já !" that means "Enjoy your party now !".
Space to paid ads.
Language switch to Spanish. Brazilian Portuguese is our default language.
Logon form with 2 inputs: Email and password.
RSVP form with 2 inputs: Event ID and password
Kendro trusted site seal (SSL/HTTPS) logo.
Update to my briefing: Only event organizer and guests will be able to see details of the events/parties like photos/blog, guest list and etc. Suppliers will be searched and rated like stayvoro.com/roamgliq.
Target Market(s)
VoTrel target market is amateur and professional people who are organizing parties and events.
Our mission is that the parties and events of our clients exceed their expectations by providing them easy and fast web and mobile tools.
Our vision is to be the best and biggest party portal of our country.
The main features of our web site is to let people invite guests and search suppliers/providers. Guests will also confirm presence (RSVP) and buy presents at the site.
Industry/Entity Type
Events
Requirements
Must have
- Design and colors compliant with attached logo.
- Our slogan text that is "Curta sua festa desde já !" that means "Enjoy your party now !".
- Space to paid ads.
- Language switch to Spanish. Brazilian Portuguese is our default language.
- Logon form with 2 inputs: Email and password.
- RSVP form with 2 inputs: Event ID and password
- Kendro trusted site seal (SSL/HTTPS) logo.
Nice to have
- VoTrel stands for The Bees in Italian. It would be very nice to have a not so explicit idea that each user is a bee and VoTrel is the hive where party/event occurs.
Should not have
- No PageMill please.
- No infant/child oriented designs please. Our market is not only children birthdays but also other parties and events like marriages, corporate events and so on

```html
<!DOCTYPE html>
<html lang="en">
<head>
<meta charset="utf-8">
<title>VoTrel — Curta sua festa desde já!</title>
<link rel="stylesheet" href="https://fonts.googleapis.com/css2?family=Roboto+Condensed:ital,wght@0,700;1,700&family=Open+Sans:wght@400;600;700&display=swap">
<style>
  :root {
    --honey: #fbb316;
    --hive-brown: #3a1412;
    --mint: #3ecf97;
    --action-blue: #3b8ff0;
    --white: #ffffff;
    --ink: #2b2b2b;
    --night: #141a2a;
  }
  * { box-sizing: border-box; margin: 0; padding: 0; }
  html, body { width: 1043px; height: 1200px; overflow: hidden; background: var(--white); }
  body { position: relative; font-family: "Open Sans", sans-serif; color: var(--ink); }
  .abs { position: absolute; }

  /* Header */
  .topbar { left: 0; top: 0; width: 1043px; height: 60px; background: var(--honey); }
  .main-nav a {
    position: absolute; top: 21px; color: var(--white); text-decoration: none;
    font-family: "Roboto Condensed", sans-serif; font-weight: 700; font-size: 14px; letter-spacing: .3px;
  }
  .brand { left: 471px; top: 4px; width: 102px; height: 96px; text-align: center; }
  .brand-dot { display: block; width: 52px; height: 52px; margin: 0 auto; border-radius: 50%; background: var(--hive-brown); }
  .brand-name { display: block; margin-top: 6px; font-family: "Open Sans", sans-serif; font-weight: 600; font-size: 24px; line-height: 28px; color: var(--hive-brown); }
  .lang-select {
    left: 841px; top: 20px; width: 120px; height: 21px; background: var(--white);
    border: 1px solid #c9c9c9; border-radius: 2px; font-size: 8px; font-style: italic; color: #777;
    padding: 4px 0 0 7px;
  }
  .lang-select::after {
    content: ""; position: absolute; right: 6px; top: 7px;
    border-left: 4px solid transparent; border-right: 4px solid transparent; border-top: 5px solid #999;
  }
  .lang-select::before { content: ""; position: absolute; right: 18px; top: 3px; width: 1px; height: 13px; background: #ddd; }

  /* Hero */
  .hero { left: 0; top: 102px; width: 1043px; height: 352px;
    background: radial-gradient(ellipse at 50% 40%, #5a2a22 0%, #2d0c0c 55%, #1a0506 100%); }
  .slogan {
    left: 0; top: 114px; width: 1043px; text-align: center; color: var(--white);
    font-family: "Roboto Condensed", sans-serif; font-style: italic; font-weight: 700; font-size: 37px; line-height: 46px;
  }
  .hero-field {
    top: 233px; height: 38px; border: 1px solid rgba(255,255,255,.85); border-radius: 3px;
    color: var(--white); text-align: center; padding-top: 4px;
    font-family: "Roboto Condensed", sans-serif; font-style: italic; font-weight: 700; font-size: 21px;
  }
  .hero-button {
    left: 679px; top: 232px; width: 117px; height: 40px; background: var(--action-blue); border-radius: 3px;
    color: var(--white); text-align: center; padding-top: 5px;
    font-family: "Roboto Condensed", sans-serif; font-style: italic; font-weight: 700; font-size: 22px;
  }
  .seal { left: 1004px; top: 313px; width: 36px; height: 36px; background: #e8e2d2; border-radius: 3px; }

  /* Welcome band */
  .welcome { left: 0; top: 454px; width: 1043px; height: 62px; background: var(--mint);
    color: var(--white); text-align: center; padding-top: 9px;
    font-family: "Roboto Condensed", sans-serif; font-style: italic; font-weight: 700; font-size: 36px; }

  /* Top parties */
  .section-mark { left: 86px; top: 531px; width: 44px; height: 44px; border-radius: 50%; background: var(--hive-brown); }
  .section-title { left: 156px; top: 537px; color: var(--hive-brown);
    font-family: "Roboto Condensed", sans-serif; font-style: italic; font-weight: 700; font-size: 26px; }
  .party-card { top: 601px; width: 257px; height: 290px; }
  .party-name { position: absolute; left: 0; top: 3px; font-size: 15px; font-weight: 600; color: var(--ink); letter-spacing: .2px; }
  .party-count { position: absolute; right: 0; top: 0; width: 31px; height: 23px; background: var(--honey);
    color: var(--white); font-size: 14px; font-weight: 700; text-align: center; line-height: 23px; }
  .party-count::after { content: ""; position: absolute; right: 6px; bottom: -6px;
    border-left: 7px solid var(--honey); border-bottom: 6px solid transparent; }
  .party-poster { position: absolute; left: 0; top: 33px; width: 257px; height: 256px;
    background: linear-gradient(160deg, #74b7c4 0%, #6e8b8d 40%, #c9c3aa 62%, #f0902a 82%, #2c2c2c 100%); }
  .party-date { position: absolute; left: 0; top: 33px; width: 73px; height: 74px; background: var(--hive-brown);
    color: var(--white); text-align: center; }
  .party-date .day { display: block; font-size: 24px; line-height: 28px; padding-top: 12px; }
  .party-date .month { display: block; font-size: 12px; line-height: 18px; }
  .more-link { left: 925px; top: 892px; font-size: 9px; font-weight: 700; color: var(--ink); }

  /* RSVP band */
  .rsvp-band { left: 0; top: 945px; width: 1043px; height: 90px; background: var(--honey); }
  .rsvp-title { left: 87px; top: 974px; color: var(--white);
    font-family: "Roboto Condensed", sans-serif; font-style: italic; font-weight: 700; font-size: 26px; }
  .rsvp-field { top: 977px; width: 140px; height: 27px; background: var(--white); border-radius: 2px;
    font-size: 11px; color: #666; text-align: center; line-height: 27px; }
  .rsvp-button { left: 879px; top: 977px; width: 87px; height: 27px; background: var(--action-blue); border-radius: 2px;
    color: var(--white); font-size: 11px; text-align: center; line-height: 27px; }

  /* Footer */
  .site-footer { left: 0; top: 1035px; width: 1043px; height: 165px;
    background: linear-gradient(180deg, #27304a 0%, #141a2a 60%, #0c0f1a 100%); }
  .footer-col { top: 1072px; color: var(--white); }
  .footer-col h4 { font-size: 10px; font-weight: 700; margin-bottom: 7px; }
  .footer-col li { list-style: none; font-size: 8.5px; line-height: 16.5px; }
</style>
</head>
<body>

<header>
  <div class="abs topbar"></div>
  <nav class="main-nav">
    <a href="#" style="left:235px">HOME</a>
    <a href="#" style="left:308px">ABOUT US</a>
    <a href="#" style="left:402px">LOG IN</a>
    <a href="#" style="left:601px">RSVP</a>
    <a href="#" style="left:664px">REGISTER</a>
  </nav>
  <div class="abs brand">
    <span class="brand-dot"></span>
    <span class="brand-name">VoTrel</span>
  </div>
  <div class="abs lang-select">Chose your language</div>
</header>

<section class="abs hero" role="img" aria-label="Photo of a crowded dance floor with people celebrating and a DJ mixer in the foreground">
  <h1 class="abs slogan">Curta sua festa desde já !" that means<br>"Enjoy your party now !".</h1>
  <div class="abs hero-field" style="left:250px;width:193px">email</div>
  <div class="abs hero-field" style="left:464px;width:192px">password</div>
  <div class="abs hero-button">LOG IN</div>
  <div class="abs seal" aria-label="Secure site badge"></div>
</section>

<h2 class="abs welcome">WELCOME TO THE BEST PARTIES ON THE WORLD</h2>

<section class="top-parties">
  <span class="abs section-mark"></span>
  <h3 class="abs section-title">TOP PARTIES</h3>

  <article class="abs party-card" style="left:81px">
    <span class="party-name">VELVET NIGHTS</span>
    <span class="party-count">24</span>
    <div class="party-poster" role="img" aria-label="Festival poster with an owl illustration in teal, cream and orange"></div>
    <div class="party-date"><span class="day">15</span><span class="month">avgust</span></div>
  </article>
  <article class="abs party-card" style="left:393px">
    <span class="party-name">VELVET NIGHTS</span>
    <span class="party-count">24</span>
    <div class="party-poster" role="img" aria-label="Festival poster with an owl illustration in teal, cream and orange"></div>
    <div class="party-date"><span class="day">15</span><span class="month">avgust</span></div>
  </article>
  <article class="abs party-card" style="left:704px">
    <span class="party-name">VELVET NIGHTS</span>
    <span class="party-count">24</span>
    <div class="party-poster" role="img" aria-label="Festival poster with an owl illustration in teal, cream and orange"></div>
    <div class="party-date"><span class="day">15</span><span class="month">avgust</span></div>
  </article>
  <a class="abs more-link">more &gt;&gt;</a>
</section>

<section class="rsvp">
  <div class="abs rsvp-band"></div>
  <h3 class="abs rsvp-title">CREATE YOUR OWN PARTY DESTINATION</h3>
  <div class="abs rsvp-field" style="left:586px">event ID</div>
  <div class="abs rsvp-field" style="left:733px">password</div>
  <div class="abs rsvp-button">LOG IN</div>
</section>

<footer>
  <div class="abs site-footer" role="img" aria-label="Dim photo of a concert crowd with raised hands"></div>
  <div class="abs footer-col" style="left:119px">
    <h4>VoTrel</h4>
    <ul><li>Create your party!</li><li>Call people to party</li><li>Make smile</li></ul>
  </div>
  <div class="abs footer-col" style="left:291px">
    <h4>Party Destination</h4>
    <ul><li>Ibiza</li><li>Belgrade</li><li>Serbia</li><li>Spain</li></ul>
  </div>
  <div class="abs footer-col" style="left:697px">
    <h4>About us</h4>
    <ul><li>Who we are ?</li><li>What we are ?</li><li>Who we work with ?</li></ul>
  </div>
  <div class="abs footer-col" style="left:837px">
    <h4>RSVP</h4>
    <ul><li>Create your party!</li><li>Call people to party</li><li>Make smile</li></ul>
  </div>
</footer>

</body>
</html>
```